Electrical company 7Kites needs a new logo design.

Need business cards for electrical company.
Modern/luxury/ Smart.
Thinking Black with White text.
Attached the logo below.

We would like two versions made - each one having different contact information on (one for each company directors). Both however will have same company address -

Fennel Court 31-35 Garwick Lane
Harlow Reach
Kentmere Vale
SS7 4PT

Contact details 1 -
Gareth Penwright
Director
gaz@7kites-demo.co.uk
07700900318

Contact details 2 -
Kieran Ashbury
Director
07700900742
kieran@7kites-demo.co.uk

Logo Text

7 Kites Electrical Solutions

```html
<!DOCTYPE html>
<html lang="en">
<head>
<meta charset="utf-8">
<title>7Kites Business Cards</title>
<link href="https://fonts.googleapis.com/css2?family=Montserrat:wght@300;400;700&display=swap" rel="stylesheet">
<style>
  :root {
    --backdrop: #1c1c1f;
    --card: #111112;
    --gold: #c9a35a;
    --white: #f4f4f2;
    --muted: #d9d9d6;
  }
  * { box-sizing: border-box; margin: 0; padding: 0; }
  html, body { width: 1200px; height: 900px; overflow: hidden; }
  body {
    background: var(--backdrop);
    font-family: "Montserrat", sans-serif;
    position: relative;
  }
  .card {
    position: absolute;
    left: 250px;
    width: 700px;
    height: 400px;
    background: var(--card);
    border-radius: 22px;
    border-bottom: 5px solid var(--gold);
    box-shadow: 0 18px 40px rgba(0,0,0,0.55);
    overflow: hidden;
  }
  .card--front { top: 40px; }
  .card--back { top: 470px; }

  .wordmark {
    position: absolute;
    color: var(--white);
    font-weight: 700;
    letter-spacing: 0;
    line-height: 1;
    white-space: nowrap;
  }
  .card--front .wordmark {
    left: 50%; top: 50%;
    transform: translate(-50%, -50%);
    font-size: 56px;
  }
  .card--back .wordmark {
    left: 60px; top: 230px;
    font-size: 38px;
  }

  .divider {
    position: absolute;
    left: 400px; top: 60px;
    width: 1.5px; height: 280px;
    background: var(--gold);
  }
  .contact {
    position: absolute;
    left: 430px; top: 70px;
    width: 250px;
    color: var(--white);
    font-size: 15px;
    line-height: 1.5;
  }
  .contact__name {
    color: var(--gold);
    font-weight: 700;
    font-size: 20px;
  }
  .contact__role { margin-bottom: 18px; font-weight: 400; }
  .contact__line {
    display: flex; align-items: center; gap: 10px;
    font-weight: 300;
    white-space: nowrap;
  }
  .contact__line svg { width: 14px; height: 14px; fill: var(--gold); flex: none; }
  .contact__address {
    margin-top: 16px;
    font-weight: 300;
    color: var(--muted);
  }
</style>
</head>
<body>
  <section class="card card--front" aria-label="Card front">
    <div class="wordmark">7Kites</div>
  </section>

  <section class="card card--back" aria-label="Card back">
    <div class="wordmark">7Kites</div>
    <div class="divider"></div>
    <div class="contact">
      <p class="contact__name">Gareth Penwright</p>
      <p class="contact__role">Director</p>
      <p class="contact__line">
        <svg viewBox="0 0 16 16" aria-hidden="true"><path d="M3.5 1.5l2.5 0 1 3.5-1.8 1.2a8 8 0 0 0 4.6 4.6L11 9l3.5 1v2.5c0 1-1 2-2 2C6.5 14.5 1.5 9.5 1.5 3.5c0-1 1-2 2-2z"/></svg>
        07700900318
      </p>
      <p class="contact__line">
        <svg viewBox="0 0 16 16" aria-hidden="true"><path d="M1 3h14v10H1z M1 3l7 6 7-6" fill="none" stroke="#c9a35a" stroke-width="1.6"/></svg>
        gaz@7kites-demo.co.uk
      </p>
      <p class="contact__address">
        Fennel Court 31-35 Garwick Lane<br>
        Harlow Reach<br>
        Kentmere Vale<br>
        SS7 4PT
      </p>
    </div>
  </section>
</body>
</html>
```